Professional Single Page Website Design for Velloway Advisory

Velloway Advisory is a new business consultancy specializing in providing expert services to small businesses, primarily in the brick-and-mortar retail and food service sectors. We offer a range of services including franchise development and launch, due diligence, and construction management.

Currently, we have a basic website set up at www.vellowayadvisory.example, but we need a professional touch to enhance its design and functionality.

Project Requirements:
- Single Page Design: For now, we need a single page design that effectively showcases who we are, our services, and contact information.
- Future Expansion: The design should be flexible and scalable for future expansion to include additional pages like specific service offerings, about us, and a dedicated contact page.
- Design Aesthetic: We are looking for a modern yet professional design that aligns with our brand identity.
- Logo: We have a logo that we like, which was also sourced from Pixel Forum. The logo files are attached to this project brief.

Key Sections to Include:
- Hero Section: An engaging introduction to Velloway Advisory with a strong visual impact.
- About Us: A brief overview of who we are and our mission.
- Team: Section for the profiles of the two principals.
- Services: A clear and concise presentation of our services, including franchise development, due diligence, and construction management.
- Contact Information: Easy-to-find contact details, including a form for inquiries.
- Call to Action: Encouraging visitors to get in touch with us for consultations or further information.

Design Considerations:
- Ensure the design is responsive and mobile-friendly.
- Include high-quality images and icons that complement our services and industry.
- We do not need development services, this is only a design project.

```html
<!DOCTYPE html>
<html lang="en">
<head>
<meta charset="utf-8">
<title>Velloway Advisory</title>
<link href="https://fonts.googleapis.com/css2?family=Poppins:wght@400;500;600&display=swap" rel="stylesheet">
<style>
:root{
  --green:#96c9b3;
  --green-dark:#7fb9a1;
  --ink:#1f2a36;
  --text:#3a4450;
  --muted:#5d6670;
  --mint:#eef7f4;
  --white:#ffffff;
  --footer:#1f2a36;
}
*{box-sizing:border-box;margin:0;padding:0}
html,body{width:1200px;height:3828px;overflow:hidden}
body{font-family:'Poppins',sans-serif;color:var(--text);background:var(--white);position:relative}
.abs{position:absolute}
.section-title{position:absolute;left:0;width:1200px;text-align:center;font-weight:500;font-size:44px;color:var(--ink)}
.section-title::after{content:"";display:block;width:48px;height:4px;background:var(--green);margin:6px auto 0;border-radius:2px}

/* header */
.site-header{position:absolute;top:0;left:0;width:1200px;height:145px;background:var(--white)}
.brand{position:absolute;display:flex;align-items:center;gap:14px}
.brand-dot{width:62px;height:62px;border-radius:50%;background:var(--green)}
.brand-name{font-weight:600;font-size:26px;line-height:1.05;color:var(--ink)}
.nav{position:absolute;left:468px;top:64px;display:flex;gap:37px;font-size:15px;font-weight:500;color:var(--ink)}
.nav .active{color:var(--green)}
.btn{display:inline-flex;align-items:center;justify-content:center;background:var(--green);color:var(--ink);font-weight:500;font-size:15px;border-radius:3px;text-transform:uppercase}
.btn-outline{background:transparent;border:2px solid var(--green)}

/* hero */
.hero{position:absolute;top:145px;left:0;width:1200px;height:600px;background:linear-gradient(100deg,#3d3a36 0%,#6b6257 40%,#a99a86 70%,#cfc3b1 100%)}
.hero h1{position:absolute;left:110px;top:170px;font-size:41px;font-weight:600;line-height:47px;color:var(--white)}
.hero p{position:absolute;left:110px;top:280px;font-size:24px;line-height:34px;color:var(--white);width:470px}
.hero .btn{position:absolute;left:111px;top:375px;width:142px;height:46px}

/* who */
.who-text{position:absolute;left:110px;top:952px;width:980px;text-align:center;font-size:16.5px;line-height:28.5px}
.mission-art{position:absolute;left:110px;top:1148px;width:427px;height:424px;border-radius:90px;transform:rotate(45deg) scale(.72);background:linear-gradient(135deg,#bfe3d6,#7fb38f 50%,#d6ece4)}
.mission h2{position:absolute;left:599px;top:1148px;font-size:45px;font-weight:500;color:var(--ink)}
.mission p{position:absolute;left:601px;width:488px;font-size:15.5px;line-height:27.3px;text-align:justify}
.mission .btn{position:absolute;left:601px;top:1515px;width:142px;height:47px;font-size:14px}

/* services */
.services{position:absolute;top:1687px;left:0;width:1200px;height:743px;background:var(--mint)}
.card{position:absolute;top:185px;width:302px;height:471px;background:var(--white);border-radius:22px;box-shadow:0 4px 14px rgba(0,0,0,.1);padding:0 24px}
.card .icon{position:absolute;left:30px;top:30px;width:86px;height:86px;border-radius:18px;background:var(--green);transform:rotate(45deg)}
.card svg{position:absolute;left:49px;top:49px}
.card h3{position:absolute;left:24px;top:145px;width:250px;font-size:17.5px;font-weight:500;line-height:25px;color:var(--ink);text-transform:uppercase}
.card p{position:absolute;left:24px;width:262px;font-size:13.5px;line-height:23.2px}
.card a{position:absolute;left:24px;top:425px;font-size:13px;color:var(--green);text-decoration:underline}
.arrow{position:absolute;top:406px}

/* team */
.team{position:absolute;top:2430px;left:0;width:1200px;height:489px;background:linear-gradient(120deg,#a6d2c0,#8fc4ad 50%,#a9d4c3)}
.member{position:absolute;top:174px;width:475px;height:231px;background:var(--white);border-radius:12px}
.member .photo{position:absolute;left:9px;top:9px;width:163px;height:213px;background:linear-gradient(160deg,#8ea3b6,#4d5864)}
.member h4{position:absolute;left:198px;top:34px;font-size:15.5px;font-weight:600;color:var(--ink)}
.member h4 span{font-weight:400;font-size:13.5px}
.member p{position:absolute;left:198px;top:66px;width:260px;font-size:11px;line-height:18.7px}
.member .icons{position:absolute;left:198px;top:156px;display:flex;gap:6px}
.circle{width:34px;height:34px;border-radius:50%;display:flex;align-items:center;justify-content:center}
.circle.fill{background:var(--green)}
.circle.line{border:1.5px solid var(--green)}

/* contact */
.info{position:absolute;left:140px;display:flex;gap:14px}
.info .badge{width:46px;height:46px;border-radius:50%;background:var(--white);box-shadow:0 4px 12px rgba(0,0,0,.12);display:flex;align-items:center;justify-content:center;margin-top:-8px}
.info h5{font-size:18px;font-weight:500;color:var(--ink)}
.info p{font-size:16px;line-height:25px}
.field{position:absolute;background:var(--white);box-shadow:0 2px 10px rgba(0,0,0,.1);font-size:14px;color:var(--ink);padding:14px 16px}

/* footer */
.footer{position:absolute;top:3540px;left:0;width:1200px;height:288px;background:var(--footer);color:var(--white)}
.footer .brand-name{color:var(--white);font-size:28px}
.fnav{position:absolute;right:111px;top:81px;display:flex;gap:38px;font-size:16px;font-weight:500}
.follow{position:absolute;right:111px;top:127px;display:flex;align-items:center;gap:8px;font-size:15px;font-weight:500}
.follow .sq{width:36px;height:36px;border-radius:50%;border:1.5px solid var(--white)}
.follow .sq.on{background:var(--green);border-color:var(--green)}
.footer hr{position:absolute;left:110px;top:221px;width:980px;border:0;border-top:1px solid #3a4552}
.copy{position:absolute;left:0;top:238px;width:1200px;text-align:center;font-size:15px}
</style>
</head>
<body>

<header class="site-header">
  <div class="brand" style="left:111px;top:41px">
    <div class="brand-dot"></div>
    <div class="brand-name">Velloway<br>Advisory</div>
  </div>
  <nav class="nav">
    <span class="active">Home</span><span>About</span><span>Services</span><span>Team</span><span>Contact</span>
  </nav>
  <a class="btn abs" style="left:937px;top:52px;width:151px;height:47px">Get in touch</a>
</header>

<section class="hero" role="img" aria-label="Two business consultants working together at a laptop in a bright office">
  <h1>Building Success<br>in Southern California</h1>
  <p>Expertise at Every Step: From Planning to Execution</p>
  <a class="btn">Learn more</a>
</section>

<h2 class="section-title" style="top:865px">Who We Are</h2>
<p class="who-text">Welcome to Velloway Advisory, your trusted partner in navigating the complexities of the real estate and small business markets. Founded by industry veterans Daniel Ferrante and Kevin Park, we specialize in providing comprehensive services tailored to the unique needs of our clients. Whether you're a franchisee, a new restaurant owner, or a commercial real estate investor, our expertise in due diligence, construction management, and investment property evaluation ensures you make informed, strategic decisions.</p>

<div class="mission-art" role="img" aria-label="Aerial view of modern buildings with greenery, framed in a rounded diamond"></div>
<section class="mission">
  <h2>Our Mission</h2>
  <p style="top:1227px">At Velloway Advisory, we are committed to your success. Our approach combines meticulous analysis, strategic insights, and personalized service to help you achieve your business goals. We pride ourselves on our ability to deliver results that exceed expectations, fostering long-term relationships built on trust and excellence.</p>
  <p style="top:1401px">Discover how Velloway Advisory can support your business journey. Partner with us and experience the difference our dedication and expertise can make.</p>
  <a class="btn btn-outline">Learn more</a>
</section>

<section class="services">
  <h2 class="section-title" style="top:78px">Our Services</h2>
  <svg class="arrow" style="left:52px" width="18" height="30" viewBox="0 0 18 30"><path d="M15 3 3 15l12 12" fill="none" stroke="#9aa3aa" stroke-width="3"/></svg>
  <svg class="arrow" style="left:1132px" width="18" height="30" viewBox="0 0 18 30"><path d="M3 3l12 12L3 27" fill="none" stroke="#1f2a36" stroke-width="3"/></svg>

  <article class="card" style="left:111px">
    <div class="icon"></div>
    <svg width="48" height="48" viewBox="0 0 48 48"><path d="M8 12h32l4 10H4z" fill="#1f2a36"/><rect x="8" y="24" width="32" height="18" fill="none" stroke="#1f2a36" stroke-width="3"/><rect x="14" y="30" width="8" height="12" fill="#1f2a36"/></svg>
    <h3>Franchise<br>Development</h3>
    <p style="top:205px">At Velloway Advisory, our Franchise Development &amp; Launch service is designed to transform your successful business into a thriving franchise. We start by thoroughly evaluating your business model to determine its franchisability. Once confirmed, our expert team handles every aspect of the franchise setup</p>
    <a>READ MORE</a>
  </article>

  <article class="card" style="left:449px">
    <div class="icon"></div>
    <svg width="48" height="48" viewBox="0 0 48 48"><circle cx="21" cy="21" r="12" fill="none" stroke="#1f2a36" stroke-width="4"/><path d="M15 21l4 4 8-8" fill="none" stroke="#1f2a36" stroke-width="3"/><path d="M30 30l10 10" stroke="#1f2a36" stroke-width="5"/></svg>
    <h3>Due Diligence</h3>
    <p style="top:180px">Velloway offers comprehensive evaluations tailored to your business needs. We meticulously assess franchise opportunities, business sales, and property transactions, identifying potential risks and liabilities to safeguard your investments. Our expert team provides actionable recommendations on deal points</p>
    <a>READ MORE</a>
  </article>

  <article class="card" style="left:787px">
    <div class="icon"></div>
    <svg width="48" height="48" viewBox="0 0 48 48"><path d="M8 26a16 16 0 0 1 32 0z" fill="#1f2a36"/><rect x="5" y="26" width="38" height="5" fill="#1f2a36"/><circle cx="24" cy="38" r="7" fill="none" stroke="#1f2a36" stroke-width="4"/></svg>
    <h3>Construction<br>Management</h3>
    <p style="top:205px">Our Building &amp; Construction Management Services oversee every aspect of your construction and development projects, from initial planning to final completion. We ensure projects stay on time and within budget, providing meticulous attention to detail and proactive problem-solving.</p>
    <a>READ MORE</a>
  </article>
</section>

<section class="team">
  <h2 class="section-title" style="top:68px">Our Team</h2>
  <article class="member" style="left:111px">
    <div class="photo" role="img" aria-label="Portrait photo of Kevin Park"></div>
    <h4>KEVIN PARK, <span>Principal</span></h4>
    <p>Kevin Park is a seasoned real estate expert with extensive experience in project and construction management, and a licensed real estate agent in California. Fluent in both English and Korean,...</p>
    <div class="icons">
      <div class="circle fill"><svg width="14" height="14" viewBox="0 0 24 24"><path d="M6 2l4 5-2 3a12 12 0 0 0 6 6l3-2 5 4-3 4C10 22 2 14 2 5z" fill="#1f2a36"/></svg></div>
      <div class="circle line"><svg width="14" height="12" viewBox="0 0 24 18"><rect width="24" height="18" rx="2" fill="#1f2a36"/><path d="M1 1l11 9 11-9" fill="none" stroke="#fff" stroke-width="2"/></svg></div>
    </div>
  </article>
  <article class="member" style="left:614px">
    <div class="photo" role="img" aria-label="Portrait photo of Daniel Ferrante" style="background:linear-gradient(160deg,#b9c9d8,#7a8a99)"></div>
    <h4>DANIEL FERRANTE, <span>Principal</span></h4>
    <p>Daniel Ferrante brings almost 20 years of rich experience as a real estate investor and a pivotal role at one of southern California's largest real estate management firms, where he...</p>
    <div class="icons">
      <div class="circle fill"><svg width="14" height="14" viewBox="0 0 24 24"><path d="M6 2l4 5-2 3a12 12 0 0 0 6 6l3-2 5 4-3 4C10 22 2 14 2 5z" fill="#1f2a36"/></svg></div>
      <div class="circle line"><svg width="14" height="12" viewBox="0 0 24 18"><rect width="24" height="18" rx="2" fill="#1f2a36"/><path d="M1 1l11 9 11-9" fill="none" stroke="#fff" stroke-width="2"/></svg></div>
    </div>
  </article>
</section>

<section class="contact">
  <h2 class="section-title" style="top:3020px">Contact Us</h2>
  <div class="info" style="top:3140px">
    <div class="badge"><svg width="14" height="18" viewBox="0 0 14 18"><path d="M7 0a7 7 0 0 1 7 7c0 5-7 11-7 11S0 12 0 7a7 7 0 0 1 7-7z" fill="#96c9b3"/><circle cx="7" cy="7" r="2.5" fill="#fff"/></svg></div>
    <div><h5>LOCATION:</h5><p>214 Harbor View Ave,<br>Coastview, CA 90000</p></div>
  </div>
  <div class="info" style="top:3248px">
    <div class="badge"><svg width="16" height="16" viewBox="0 0 24 24"><path d="M6 2l4 5-2 3a12 12 0 0 0 6 6l3-2 5 4-3 4C10 22 2 14 2 5z" fill="#96c9b3"/></svg></div>
    <div><h5>PHONE:</h5><p>+1 (555) 010 2040</p></div>
  </div>
  <div class="info" style="top:3338px">
    <div class="badge"><svg width="18" height="18" viewBox="0 0 18 18"><circle cx="9" cy="9" r="7" fill="none" stroke="#96c9b3" stroke-width="2"/><path d="M9 4v5h4" fill="none" stroke="#96c9b3" stroke-width="2"/></svg></div>
    <div><h5>EMAIL:</h5><p>info@vellowayadvisory.example</p></div>
  </div>

  <div class="field" style="left:465px;top:3128px;width:292px;height:47px">First Name</div>
  <div class="field" style="left:767px;top:3128px;width:292px;height:47px">Last Name</div>
  <div class="field" style="left:465px;top:3189px;width:292px;height:47px">Email</div>
  <div class="field" style="left:767px;top:3189px;width:292px;height:47px">Phone</div>
  <div class="field" style="left:465px;top:3250px;width:594px;height:107px">Message...</div>
  <a class="btn abs" style="left:671px;top:3372px;width:180px;height:47px">Send message</a>
</section>

<footer class="footer">
  <div class="brand" style="left:111px;top:70px">
    <div class="brand-dot" style="width:70px;height:70px"></div>
    <div class="brand-name">Velloway<br>Advisory</div>
  </div>
  <nav class="fnav"><span>Home</span><span>/</span><span>About</span><span>/</span><span>Services</span><span>/</span><span>Team</span><span>/</span><span>Contact</span></nav>
  <div class="follow"><span style="margin-right:14px">Follow Us:</span><div class="sq on"></div><div class="sq"></div><div class="sq"></div></div>
  <hr>
  <p class="copy">© 2024 Velloway Advisory &nbsp; / &nbsp; All Rights Reserved</p>
</footer>

</body>
</html>
```